Business Coaching Model and Flow Chart

We need this flowchart, attached, to be updated in a modern and engaging way. This flowchart is the cornerstone of a business coaching class we are running, and will be the main support reference for the people who take the class. We are open to ideas as to how it is presented, but we would like a largely minimalist look that leaves space to be impactful where the key information sites. Our colour scheme is primary red (D51C29), white, grey (333333), black, and secondary green (3C8740). We will also need our logo present (attached).

```html
<!DOCTYPE html>
<html lang="en">
<head>
<meta charset="utf-8">
<title>Groups to Teams – Coaching Model</title>
<link href="https://fonts.googleapis.com/css2?family=Open+Sans:wght@400;600;700;800&display=swap" rel="stylesheet">
<style>
:root{
  --red:#d51c29;
  --green:#3c8740;
  --grey:#333333;
  --black:#111111;
  --white:#ffffff;
}
*{box-sizing:border-box;margin:0;padding:0}
html,body{width:1168px;height:1200px;overflow:hidden;background:var(--white)}
body{position:relative;font-family:"Open Sans",Arial,sans-serif;color:var(--black)}

.brand{position:absolute;left:0;width:1168px;top:222px;text-align:center;font-weight:600;font-size:20px;letter-spacing:.5px;color:var(--grey)}

.title{position:absolute;left:0;width:1168px;top:290px;text-align:center;font-weight:800;font-size:37px;line-height:33px;letter-spacing:-.3px}

.stage{position:absolute;top:402px;width:100px;height:100px;border-radius:50%;background:var(--black);color:var(--white);display:flex;align-items:center;justify-content:center;text-align:center;font-weight:700;font-size:12px;line-height:13px;padding:0 4px;white-space:nowrap}
.stage--problem{background:var(--red);font-size:18px;font-weight:800}
.stage--solution{background:var(--green);font-size:18px;font-weight:800}
.connector{position:absolute;top:444px;width:15px;height:15px}

.column{position:absolute;top:514px;width:102px;height:456px;background:var(--grey);border-radius:5px;padding:7px 8px;display:flex;flex-direction:column;gap:6px}
.step{background:var(--black);color:var(--white);border-radius:4px;height:50px;display:flex;flex-direction:column;align-items:center;justify-content:center;text-align:center;font-size:10px;line-height:11.5px;padding:0 2px}
.step--tall{height:147px;justify-content:flex-start;padding-top:12px}
.step--tall .sub{font-size:8px;line-height:16px}
.step--tall .lead{margin-bottom:12px}
.step--learn{height:198px;justify-content:flex-start;padding-top:8px}
.step--learn .lead{margin-bottom:4px}
.step--learn .sub{font-size:8px;line-height:16.5px}
.column--reflect{gap:5px}
.column--reflect .step{height:36px}

.tile{border-radius:3px;height:50px;color:var(--white);display:flex;flex-direction:column;align-items:center;justify-content:flex-end;text-align:center;font-size:9.5px;line-height:8.5px;padding:0 3px 5px;gap:4px}
.tile--problem{background:var(--red)}
.tile--solution{background:var(--green)}
.tile .icon{width:20px;height:20px;border:1.5px solid rgba(255,255,255,.85);border-radius:4px}
</style>
</head>
<body>

<div class="brand">Maren Holt</div>

<h1 class="title">Groups to Teams<br>Through Learning Together</h1>

<div class="stage stage--problem" style="left:154px">PROBLEM</div>
<div class="stage" style="left:275px">Clarify<br>challenges -<br>Diagnostics</div>
<div class="stage" style="left:401px">Planning For<br>Success<br>Make A Plan</div>
<div class="stage" style="left:523px">Learn the<br>tools Workshop</div>
<div class="stage" style="left:648px">Doing<br>Mastering<br>The Tools</div>
<div class="stage" style="left:771px">Reflect -<br>Adapt - Embed</div>
<div class="stage stage--solution" style="left:896px">SOLUTION</div>

<svg class="connector" style="left:257px" viewBox="0 0 16 16"><circle cx="8" cy="8" r="8" fill="#111"/><path d="M4 8h7M8 5l3 3-3 3" stroke="#fff" stroke-width="1.6" fill="none"/></svg>
<svg class="connector" style="left:380px" viewBox="0 0 16 16"><circle cx="8" cy="8" r="8" fill="#111"/><path d="M4 8h7M8 5l3 3-3 3" stroke="#fff" stroke-width="1.6" fill="none"/></svg>
<svg class="connector" style="left:504px" viewBox="0 0 16 16"><circle cx="8" cy="8" r="8" fill="#111"/><path d="M4 8h7M8 5l3 3-3 3" stroke="#fff" stroke-width="1.6" fill="none"/></svg>
<svg class="connector" style="left:628px" viewBox="0 0 16 16"><circle cx="8" cy="8" r="8" fill="#111"/><path d="M4 8h7M8 5l3 3-3 3" stroke="#fff" stroke-width="1.6" fill="none"/></svg>
<svg class="connector" style="left:752px" viewBox="0 0 16 16"><circle cx="8" cy="8" r="8" fill="#111"/><path d="M4 8h7M8 5l3 3-3 3" stroke="#fff" stroke-width="1.6" fill="none"/></svg>
<svg class="connector" style="left:876px" viewBox="0 0 16 16"><circle cx="8" cy="8" r="8" fill="#111"/><path d="M4 8h7M8 5l3 3-3 3" stroke="#fff" stroke-width="1.6" fill="none"/></svg>

<div class="column" style="left:154px">
  <div class="tile tile--problem"><span class="icon" role="img" aria-label="Invoice icon"></span>Underbilling</div>
  <div class="tile tile--problem"><span class="icon" role="img" aria-label="Team icon"></span>Staff Retention</div>
  <div class="tile tile--problem"><span class="icon" role="img" aria-label="Search person icon"></span>Hard to recruit</div>
  <div class="tile tile--problem"><span class="icon" role="img" aria-label="Complaint speech icon"></span>Client Complaints</div>
  <div class="tile tile--problem"><span class="icon" role="img" aria-label="Stress icon"></span>Staff Stress and Burnout</div>
  <div class="tile tile--problem"><span class="icon" role="img" aria-label="Conflict icon"></span>Conflict</div>
  <div class="tile tile--problem"><span class="icon" role="img" aria-label="Crossing arrows icon"></span>CCSA Constant Change</div>
  <div class="tile tile--problem"><span class="icon" role="img" aria-label="Hourglass icon"></span>Limited in Best Practice</div>
</div>

<div class="column" style="left:275px">
  <div class="step">Scoping</div>
  <div class="step">Interviews</div>
  <div class="step">Group<br>reflection</div>
  <div class="step">Opinion Surveys</div>
  <div class="step step--tall">
    <span class="lead">Certified<br>Assessments</span>
    <span class="sub">Personality Styles</span>
    <span class="sub">Work Preference</span>
    <span class="sub">Strenghts &amp; Values</span>
    <span class="sub">Trust</span>
    <span class="sub">360</span>
  </div>
</div>

<div class="column" style="left:401px">
  <div class="step">Team data<br>analysis<br>workshop</div>
  <div class="step">Individual<br>Development<br>Plan</div>
  <div class="step">Team<br>Development<br>Plan</div>
  <div class="step">Organisational<br>Plan</div>
</div>

<div class="column" style="left:524px">
  <div class="step step--learn">
    <span class="lead">Foundation<br>Workshops</span>
    <span class="sub" style="line-height:9px;margin-bottom:4px">Difficult<br>Conversations</span>
    <span class="sub">Giving &amp; Receiving</span>
    <span class="sub">Feedback</span>
    <span class="sub">Values Alignment</span>
    <span class="sub">Shared Purpose</span>
    <span class="sub">Ways of Working</span>
    <span class="sub">Diversity</span>
    <span class="sub">Wellbeing</span>
    <span class="sub">Time Management</span>
  </div>
  <div class="step">Customised<br>Workshops</div>
</div>

<div class="column" style="left:648px">
  <div class="step">Group Coaching</div>
  <div class="step">Team Coaching</div>
  <div class="step">Individual<br>Coaching</div>
  <div class="step">Peer Learning</div>
  <div class="step">Lunch ‘n Learn</div>
</div>

<div class="column column--reflect" style="left:770px">
  <div class="step">Culture Comittee</div>
  <div class="step">Embedding<br>Workshop</div>
  <div class="step">Culture<br>Collateral</div>
  <div class="step">WOW Manifesto</div>
  <div class="step">Leadership<br>Team Coaching</div>
  <div class="step">Measure ROI</div>
  <div class="step">Review Success</div>
  <div class="step">Evaluation<br>Surveys</div>
  <div class="step">Temperature<br>Checks</div>
  <div class="step">Recruitt To Suit</div>
  <div class="step">Future Proofing -<br>what next?</div>
</div>

<div class="column" style="left:896px">
  <div class="tile tile--solution"><span class="icon" role="img" aria-label="Person icon"></span>Self awareness &amp; Ownership</div>
  <div class="tile tile--solution"><span class="icon" role="img" aria-label="Handshake icon"></span>Partnership</div>
  <div class="tile tile--solution"><span class="icon" role="img" aria-label="Workplace icon"></span>Great Place To Work</div>
  <div class="tile tile--solution"><span class="icon" role="img" aria-label="Growing plant icon"></span>Growth Mindset</div>
  <div class="tile tile--solution"><span class="icon" role="img" aria-label="Megaphone icon"></span>Coach Approach Culture</div>
  <div class="tile tile--solution"><span class="icon" role="img" aria-label="Feedback icon"></span>Feedback Culture</div>
  <div class="tile tile--solution"><span class="icon" role="img" aria-label="Network icon"></span>Way To Manage Conflict</div>
  <div class="tile tile--solution"><span class="icon" role="img" aria-label="Speech bubbles icon"></span>Best Practice Communication Skills</div>
</div>

</body>
</html>
```